I need a business card for myself, being a proprietor of a funeral parlor based in Manila. I'd like the card to have either of the following:
White Font on Black Background
or
Black Font on White Background
No logo is needed however I will appreciate any efforts to show a symbol of eternal happiness, aptly designed with above mentioned colors in mind.
Company name, address and contact on the lower right corner.
Logo or symbol anywhere.
Quillstone Funeral Services
+639174826351
darvik4521@pelmora.com
corner of Brisco Avenue and Velhurst Street
Harlow City, Estoria
Thank you.
Update: Please include a small dove in your design. You are free to choose where you would like it on the card.

```html
<!DOCTYPE html>
<html lang="en">
<head>
<meta charset="utf-8">
<title>Quillstone Funeral Services – Business Card</title>
<link href="https://fonts.googleapis.com/css2?family=Cinzel:wght@400;500&display=swap" rel="stylesheet">
<style>
  :root {
    --backdrop: #e6e6e6;
    --card-black: #0b0b0b;
    --card-glow: #2e2e2e;
    --ink-white: #f4f4f4;
    --ink-soft: #d9d9d9;
  }
  * { margin: 0; padding: 0; box-sizing: border-box; }
  html, body {
    width: 1200px;
    height: 900px;
    overflow: hidden;
  }
  body {
    background: radial-gradient(ellipse at 50% 45%, #f2f2f2 0%, var(--backdrop) 70%);
    display: flex;
    align-items: center;
    justify-content: center;
    font-family: "Cinzel", "Trajan Pro", serif;
  }
  .business-card {
    position: relative;
    width: 980px;
    height: 560px;
    background: radial-gradient(ellipse at 45% 10%, var(--card-glow) 0%, #161616 40%, var(--card-black) 85%);
    overflow: hidden;
    box-shadow: 0 18px 40px rgba(0,0,0,0.25);
  }
  .floral-motif {
    position: absolute;
    left: 330px;
    top: 170px;
    width: 650px;
    height: 390px;
    background: radial-gradient(ellipse at 55% 55%, rgba(110,110,110,0.35) 0%, rgba(80,80,80,0.18) 45%, rgba(60,60,60,0) 75%);
  }
  .brand {
    position: absolute;
    left: 70px;
    top: 60px;
    display: flex;
    align-items: flex-start;
    gap: 34px;
  }
  .brand-mark {
    width: 84px;
    height: 84px;
    border-radius: 50%;
    background: var(--ink-white);
    flex-shrink: 0;
    margin-top: 8px;
  }
  .brand-name {
    color: var(--ink-white);
    font-size: 44px;
    font-weight: 500;
    line-height: 1.12;
    letter-spacing: 0.5px;
  }
  .contact {
    position: absolute;
    left: 188px;
    top: 210px;
    color: var(--ink-soft);
    font-size: 20px;
    font-weight: 400;
    line-height: 1.35;
    letter-spacing: 0.4px;
  }
  .contact-phone { margin-bottom: 26px; }
  .contact-email { margin-bottom: 34px; text-transform: lowercase; }
</style>
</head>
<body>
  <div class="business-card">
    <div class="floral-motif" role="img" aria-label="Faint grey line-art floral pattern with blossoms, leaves and dotted sprays"></div>

    <div class="brand">
      <span class="brand-mark" aria-hidden="true"></span>
      <h1 class="brand-name">Quillstone<br>Funeral Services</h1>
    </div>

    <div class="contact">
      <p class="contact-phone">+639174826351</p>
      <p class="contact-email">darvik4521@pelmora.com</p>
      <p class="contact-address">corner of Brisco Avenue and<br>Velhurst Street Harlow City, Estoria</p>
    </div>
  </div>
</body>
</html>
```